Portal Panel Medic need professional looking business card printed on plastic, Commericial, Industri

We are family owned and operated garage door company in Indianapolis, Indiana. We sale service and install dock equipment, doors, operators. We are looking to expand our commercial/ industrial division. We also service all residential doors and operators. We are looking for a business that stands out of the crowd. We are committed to have the best customer service in the industry.

Target Market(s)

National and local general contractors, National/ Corpate service accounts,

Industry/Entity Type

Business Service

Contact Information for Business Card

To be printed on plastic stock

Font styles to use
Sans Serif

Colors
ffffff
f04a50
ec1f27

Requirements
Must have
• Name, website,email, phone number, position.
Nice to have
• A standout professional design

```html
<!DOCTYPE html>
<html lang="en">
<head>
<meta charset="utf-8">
<title>Portal Panel Medic – Business Card</title>
<link rel="stylesheet" href="https://fonts.googleapis.com/css2?family=Roboto:wght@400;500;700;900&family=Dancing+Script:wght@600&display=swap">
<style>
  :root {
    --bg: #2a2a2c;
    --card-white: #ffffff;
    --card-black: #050505;
    --red: #ec1f27;
    --red-soft: #f04a50;
    --ink: #1c1c1c;
    --rule: #222222;
  }
  * { box-sizing: border-box; margin: 0; padding: 0; }
  html, body { width: 1200px; height: 865px; overflow: hidden; }
  body {
    background: var(--bg);
    font-family: "Roboto", Arial, sans-serif;
    position: relative;
  }
  .card {
    position: absolute;
    top: 278px;
    width: 540px;
    height: 310px;
    border-radius: 22px;
    overflow: hidden;
  }
  .card--front { left: 40px; background: var(--card-white); color: var(--ink); }
  .card--back { left: 620px; background: var(--card-black); }

  .wordmark {
    position: absolute;
    left: 0; right: 0;
    display: flex;
    justify-content: center;
    align-items: center;
    gap: 10px;
    font-weight: 900;
    color: var(--red);
    text-transform: uppercase;
    letter-spacing: 0.5px;
  }
  .wordmark__square { width: 18px; height: 18px; background: var(--red); }
  .card--front .wordmark { top: 78px; font-size: 34px; }

  .rule { position: absolute; height: 1.5px; background: var(--rule); }
  .rule--name { left: 28px; top: 150px; width: 300px; }
  .rule--contact { left: 250px; top: 222px; width: 262px; }

  .person {
    position: absolute;
    left: 28px; top: 166px;
    display: flex; align-items: flex-start; gap: 10px;
  }
  .person__divider { width: 1.5px; height: 40px; background: var(--rule); }
  .person__name { font-size: 20px; font-weight: 500; letter-spacing: 1.5px; text-transform: uppercase; }
  .person__role { font-size: 13px; color: var(--red); letter-spacing: 1px; text-transform: uppercase; margin-top: 3px; }

  .contacts {
    position: absolute;
    left: 258px; top: 190px;
    list-style: none;
    font-size: 17px;
    line-height: 1;
  }
  .contacts li { display: flex; align-items: center; gap: 12px; height: 30px; }
  .contacts li:nth-child(2) { margin-top: 10px; }
  .contacts svg { width: 16px; height: 16px; flex: none; }

  .card--back .wordmark { top: 88px; font-size: 36px; }
  .tagline {
    position: absolute; left: 0; right: 0; top: 150px;
    text-align: center;
    font-family: "Dancing Script", cursive;
    font-size: 20px; color: var(--red-soft);
  }
  .back-phone {
    position: absolute; left: 0; right: 0; top: 192px;
    text-align: center;
    font-size: 44px; font-weight: 500; color: var(--red);
    letter-spacing: 1px;
  }
</style>
</head>
<body>

<section class="card card--front" aria-label="Business card front">
  <div class="wordmark"><span class="wordmark__square"></span>Portal Panel Medic</div>
  <div class="rule rule--name"></div>
  <div class="person">
    <svg width="16" height="16" viewBox="0 0 16 16" aria-hidden="true"><circle cx="8" cy="5" r="3.5" fill="var(--red)"/><path d="M1 16c0-4 3-6.5 7-6.5s7 2.5 7 6.5z" fill="var(--red)"/></svg>
    <span class="person__divider"></span>
    <div>
      <div class="person__name">Martin Hollace</div>
      <div class="person__role">Managing Director</div>
    </div>
  </div>
  <div class="rule rule--contact"></div>
  <ul class="contacts">
    <li>
      <svg viewBox="0 0 16 16" aria-hidden="true"><path d="M3.5 1l3 3-1.8 1.8c.8 2 2.5 3.7 4.5 4.5L11 8.5l3 3-2 2.5C6 13.5 2.5 10 1 4z" fill="var(--red)"/></svg>
      1300 555 019
    </li>
    <li>
      <svg viewBox="0 0 16 16" aria-hidden="true"><rect x="1" y="3" width="14" height="10" fill="var(--red)"/><path d="M1 3l7 6 7-6" stroke="#fff" stroke-width="1.3" fill="none"/></svg>
      info@portalpanelmedic.com
    </li>
    <li>
      <svg viewBox="0 0 16 16" aria-hidden="true"><g fill="none" stroke="var(--red)" stroke-width="1.3"><circle cx="8" cy="8" r="6.5"/><ellipse cx="8" cy="8" rx="3" ry="6.5"/><path d="M1.5 8h13M2.5 4.8h11M2.5 11.2h11"/></g></svg>
      www.portalpanelmedic.com
    </li>
  </ul>
</section>

<section class="card card--back" aria-label="Business card back">
  <div class="wordmark"><span class="wordmark__square"></span>Portal Panel Medic</div>
  <div class="tagline">“Expert Service at an Affordable Price”</div>
  <div class="back-phone">(317) 555-0142</div>
</section>

</body>
</html>
```